Online medical reviews website needs banner advert!

We need banner advert templates for our website, www.traineepanel.net. These should meet the technical requirements of our partner (uploaded).

Our groundbreaking website allows doctors in training to rate and review their training.

The adverts should use the same modern design language and colour scheme as our website. They should use the text 'Help a junior doctor make a big decision - rate your training!'.

Vector assets should be supplied, allowing us to use alternative text in future.
Updates

Industry/Entity Type

Healthcare

Font styles to use
Other font styles liked:
• Karla

Colors
3277b5
0555a3
ffffff

Requirements
Must have
• Similar design to our website. Should be elegant & modern. Must allow future text to be easily inserted.
Should not have
• Unrelated design.

```html
<!DOCTYPE html>
<html lang="en">
<head>
<meta charset="utf-8">
<title>Trainee Panel – Banner Variations</title>
<link href="https://fonts.googleapis.com/css2?family=Karla:wght@400;700&family=Roboto:wght@400&display=swap" rel="stylesheet">
<style>
  :root {
    --brand-blue: #0555a3;
    --brand-mid: #3277b5;
    --white: #ffffff;
    --canvas: #f2f2f2;
    --cta: #0a7cf5;
    --cta-edge: #0757b8;
    --photo-top: #3e5378;
    --photo-mid: #30476e;
    --photo-low: #3a4e70;
    --label: #1a1a1a;
  }
  * { box-sizing: border-box; margin: 0; padding: 0; }
  html, body { width: 1200px; height: 800px; overflow: hidden; background: var(--canvas); }
  .board { position: relative; width: 1200px; height: 800px; }

  .banner {
    position: absolute;
    width: 240px;
    height: 480px;
    background: var(--white);
    overflow: hidden;
    box-shadow: 0 8px 12px rgba(0,0,0,0.28);
    font-family: "Karla", sans-serif;
  }
  .banner--v1 { left: 64px;  top: 72px; }
  .banner--v2 { left: 342px; top: 74px; }
  .banner--v3 { left: 618px; top: 72px; }
  .banner--v4 { left: 896px; top: 72px; }

  .banner__header {
    position: absolute; left: 0; top: 0; width: 100%; height: 60px;
    background: var(--brand-blue);
    display: flex; align-items: center; justify-content: center;
  }
  .brand-name {
    color: var(--white);
    font-family: "Karla", sans-serif;
    font-weight: 400;
    font-size: 22px;
    letter-spacing: -0.5px;
  }

  .banner__photo {
    position: absolute; left: 0; width: 100%;
    background: linear-gradient(180deg, var(--photo-top) 0%, var(--photo-mid) 45%, var(--photo-low) 75%, #34486a 100%);
  }
  .banner--v1 .banner__photo { top: 60px; height: 420px; }
  .banner--v2 .banner__photo { top: 60px; height: 360px; }
  .banner--v3 .banner__photo { top: 74px; height: 406px; }
  .banner--v4 .banner__photo { top: 72px; height: 336px; }

  .headline {
    position: absolute; left: 0; width: 100%;
    color: var(--white);
    font-weight: 700;
    font-size: 17.5px;
    line-height: 25.6px;
    letter-spacing: 0.8px;
    text-align: center;
    text-transform: uppercase;
  }
  .banner--v1 .headline, .banner--v3 .headline { top: 171px; }
  .banner--v2 .headline { top: 171px; }
  .banner--v4 .headline { top: 169px; }

  .cta {
    position: absolute; left: 42px;
    width: 156px; height: 31px;
    background: var(--cta);
    border-bottom: 2px solid var(--cta-edge);
    color: var(--white);
    font-weight: 700;
    font-size: 12.5px;
    letter-spacing: 0.4px;
    display: flex; align-items: center; justify-content: center;
  }
  .banner--v1 .cta, .banner--v3 .cta { top: 402px; }
  .banner--v2 .cta { top: 342px; }
  .banner--v4 .cta { top: 426px; }

  .banner__footer {
    position: absolute; left: 0; top: 420px; width: 100%; height: 60px;
    background: var(--brand-blue);
    display: flex; align-items: center; justify-content: center;
  }
  .site-url {
    color: var(--white);
    font-size: 10.5px;
    letter-spacing: 0.4px;
  }

  .version-label {
    position: absolute; top: 624px;
    width: 80px; margin-left: -40px;
    text-align: center;
    font-family: "Roboto", sans-serif;
    font-size: 23px;
    color: var(--label);
  }
</style>
</head>
<body>
<main class="board">

  <section class="banner banner--v1">
    <header class="banner__header"><span class="brand-name">Trainee Panel</span></header>
    <div class="banner__photo" role="img" aria-label="Hospital building entrance with a parked ambulance, tinted blue"></div>
    <h2 class="headline">Help a junior<br>doctor make<br>a big decision</h2>
    <div class="cta">Rate your training!</div>
  </section>

  <section class="banner banner--v2">
    <header class="banner__header"><span class="brand-name">Trainee Panel</span></header>
    <div class="banner__photo" role="img" aria-label="Hospital building entrance with a parked ambulance, tinted blue"></div>
    <h2 class="headline">Help a junior<br>doctor make<br>a big decision</h2>
    <div class="cta">Rate your training!</div>
    <footer class="banner__footer"><span class="site-url">www.traineepanel.net</span></footer>
  </section>

  <section class="banner banner--v3">
    <header class="banner__header"><span class="brand-name">Trainee Panel</span></header>
    <div class="banner__photo" role="img" aria-label="Hospital building entrance with a parked ambulance, tinted blue"></div>
    <h2 class="headline">Help a junior<br>doctor make<br>a big decision</h2>
    <div class="cta">Rate your training!</div>
  </section>

  <section class="banner banner--v4">
    <header class="banner__header"><span class="brand-name">Trainee Panel</span></header>
    <div class="banner__photo" role="img" aria-label="Hospital building entrance with a parked ambulance, tinted blue"></div>
    <h2 class="headline">Help a junior<br>doctor make<br>a big decision</h2>
    <div class="cta">Rate your training!</div>
  </section>

  <p class="version-label" style="left:176px">v1</p>
  <p class="version-label" style="left:448px">v2</p>
  <p class="version-label" style="left:738px">v3</p>
  <p class="version-label" style="left:1016px">v4</p>

</main>
</body>
</html>
```